Harvest Ledger Group
Business Cards, Envelopes and Letterhead
Project: Harvest Ledger Group
Harvest Ledger Group -
Creative Brief
Bright & Fun-filled
Marcus T. Halvorsen
President
47 Brookmere Loop West, Suite B318 Englewood, CO 80214
mh@kt-assetpartners.com
www.kt-assetpartners.com

```html
<!DOCTYPE html>
<html lang="en">
<head>
<meta charset="utf-8">
<title>Harvest Ledger Group – Stationery</title>
<link rel="stylesheet" href="https://fonts.googleapis.com/css2?family=Tinos:wght@400;700&display=swap">
<style>
  :root{
    --bg:#2a2a2c;
    --paper:#ffffff;
    --paper-shade:#eef0f3;
    --blue:#1f5fb8;
    --blue-deep:#0c2f74;
    --navy:#071d4d;
    --silver:#c9ced6;
    --ink:#1d2a44;
    --muted:#6a7385;
    --rule:#b9c4d6;
  }
  *{box-sizing:border-box;margin:0;padding:0}
  html,body{width:1200px;height:1057px;overflow:hidden;background:var(--bg)}
  body{font-family:"Tinos",serif;color:var(--ink);position:relative}
  .piece{position:absolute;overflow:hidden}
  .brand{display:flex;align-items:center;gap:6px;font-family:"Tinos",serif;font-weight:700;text-transform:uppercase;letter-spacing:.04em;white-space:nowrap;z-index:2}
  .brand-mark{width:10px;height:10px;background:currentColor;flex:none}
  .brand.on-light{color:var(--blue-deep)}
  .brand.on-dark{color:#fff}
  .artwork{position:absolute;z-index:1;background:linear-gradient(135deg,var(--silver) 0%,#8aa3cc 30%,var(--blue) 60%,var(--blue-deep) 100%)}

  /* business card front */
  .card-front{left:43px;top:96px;width:247px;height:130px;background:var(--paper)}
  .card-front .brand{position:absolute;left:12px;top:12px;font-size:10px}
  .card-front .brand-mark{width:7px;height:7px}
  .card-front .person{position:absolute;left:12px;top:34px;font-size:9px;line-height:1.3}
  .card-front .person strong{display:block;font-size:10px}
  .card-front .details{position:absolute;left:12px;top:62px;width:130px;font-size:6.5px;line-height:1.35;color:var(--muted)}
  .card-front .artwork{right:0;top:0;width:80px;height:130px;clip-path:polygon(40% 0,100% 0,100% 100%,0 100%,10% 50%)}
  .card-front .footer-band{position:absolute;left:0;bottom:0;width:100%;height:8px;background:var(--blue-deep);z-index:2}

  /* business card back */
  .card-back{left:310px;top:96px;width:247px;height:130px;background:linear-gradient(120deg,var(--blue-deep),var(--navy))}
  .card-back .brand{position:absolute;left:16px;top:18px;font-size:10px}
  .card-back .brand-mark{width:7px;height:7px}
  .card-back .artwork{right:0;top:0;width:80px;height:130px;clip-path:polygon(40% 0,100% 0,100% 100%,0 100%)}

  /* envelope */
  .envelope{left:580px;top:96px;width:568px;height:223px;background:var(--paper)}
  .envelope .brand{position:absolute;left:22px;top:20px;font-size:14px}
  .envelope .return{position:absolute;left:22px;top:42px;font-size:7px;line-height:1.4;color:var(--muted);width:200px}
  .envelope .artwork{right:0;top:0;width:190px;height:223px;clip-path:polygon(45% 0,100% 0,100% 100%,5% 100%,0 60%)}
  .envelope .web{position:absolute;left:22px;bottom:10px;font-size:7px;color:var(--muted)}
  .envelope .footer-band{position:absolute;left:0;bottom:0;width:100%;height:4px;background:var(--blue);z-index:2}

  /* letterhead */
  .letterhead{left:35px;top:255px;width:525px;height:783px;background:var(--paper)}
  .letterhead .brand{position:absolute;left:30px;top:26px;font-size:18px}
  .letterhead .brand-mark{width:13px;height:13px}
  .letterhead .artwork{right:0;top:0;width:140px;height:92px;clip-path:polygon(0 0,100% 0,100% 100%,50% 60%)}
  .letterhead .artwork.lower{top:auto;bottom:0;width:150px;height:190px;clip-path:polygon(100% 0,100% 100%,0 100%,40% 55%)}
  .letter-body{position:absolute;left:55px;top:120px;width:375px;font-size:9px;line-height:1.55;color:#3a3f4a}
  .letter-body .salutation{font-weight:700;margin-bottom:16px;color:var(--ink)}
  .letter-body p{margin-bottom:14px}
  .letterhead .sign-block{position:absolute;left:30px;bottom:20px;font-size:7px;line-height:1.4;color:var(--muted)}
  .letterhead .footer-band{position:absolute;left:0;bottom:0;width:100%;height:6px;background:var(--blue);z-index:2}

  /* CD folder and disc */
  .cd-folder{left:586px;top:368px;width:290px;height:290px}
  .cd-folder svg{position:absolute;left:0;top:0}
  .cd-folder .brand{position:absolute;left:26px;top:26px;font-size:12px}
  .cd-disc{left:841px;top:392px;width:275px;height:275px;border-radius:50%;background:radial-gradient(circle at 50% 50%,var(--bg) 0 9%,var(--silver) 9% 12%,transparent 12%),linear-gradient(90deg,var(--blue) 0 50%,var(--paper-shade) 50%)}
  .cd-disc .artwork{left:0;top:0;width:275px;height:275px;border-radius:50%;clip-path:polygon(0 0,55% 0,45% 100%,0 100%);mask:radial-gradient(circle,transparent 0 13%,#000 13%)}
  .cd-disc .web{position:absolute;left:18px;top:126px;font-size:6px;color:#fff;transform:rotate(-90deg);transform-origin:left top;z-index:2}

  /* CD sleeve envelope */
  .sleeve{left:574px;top:667px;width:290px;height:320px;background:var(--paper)}
  .sleeve .flap{position:absolute;left:0;top:0;width:100%;height:116px;background:linear-gradient(120deg,var(--blue-deep),var(--blue))}
  .sleeve .brand{position:absolute;left:30px;top:40px;font-size:12px}
  .sleeve .note-lines{position:absolute;left:46px;top:150px;width:198px;height:120px;border:1px solid var(--rule);border-radius:6px;background:repeating-linear-gradient(to bottom,transparent 0 14px,var(--rule) 14px 15px)}
  .sleeve .web{position:absolute;left:0;right:0;bottom:16px;text-align:center;font-size:7px;color:var(--muted)}

  /* standalone logo lockup */
  .logo-lockup{left:935px;top:800px;width:240px;text-align:center}
  .logo-lockup .brand{justify-content:center;font-size:13px}
  .logo-lockup .tagline{margin-top:6px;font-size:5.5px;letter-spacing:.08em;color:#fff;text-transform:uppercase}
</style>
</head>
<body>

<section class="piece card-front" aria-label="Business card front">
  <div class="brand on-light"><span class="brand-mark"></span>Harvest Ledger Group</div>
  <div class="person"><strong>Marcus T. Halvorsen</strong>President</div>
  <div class="details">47 Brookmere Loop West, Suite B318<br>Englewood, CO 80214<br>mh@kt-assetpartners.com<br>www.kt-assetpartners.com</div>
  <div class="artwork" role="img" aria-label="Blue block and silver arrow graphic"></div>
  <div class="footer-band"></div>
</section>

<section class="piece card-back" aria-label="Business card back">
  <div class="brand on-dark"><span class="brand-mark"></span>Harvest Ledger Group</div>
  <div class="artwork" role="img" aria-label="Blue block and silver arrow graphic"></div>
</section>

<section class="piece envelope" aria-label="Envelope">
  <div class="brand on-light"><span class="brand-mark"></span>Harvest Ledger Group</div>
  <div class="return">47 Brookmere Loop West, Suite B318<br>Englewood, CO 80214</div>
  <div class="web">www.kt-assetpartners.com</div>
  <div class="artwork" role="img" aria-label="Blue block and silver arrow graphic"></div>
  <div class="footer-band"></div>
</section>

<section class="piece letterhead" aria-label="Letterhead">
  <div class="brand on-light"><span class="brand-mark"></span>Harvest Ledger Group</div>
  <div class="artwork" role="img" aria-label="Blue block and silver arrow graphic"></div>
  <div class="letter-body">
    <p class="salutation">Dear Sirs</p>
    <p>We have reviewed your application with care and are pleased to confirm that your planning file is now open with our team. Thank you for choosing us to guide the next stage of your financial journey.</p>
    <p>Should you wish to discuss any detail, please call our office and an advisor will arrange a time that suits you. We look forward to working together over the coming months.</p>
    <p>We have reviewed your application with care and are pleased to confirm that your planning file is now open with our team. Thank you for choosing us to guide the next stage of your financial journey.</p>
    <p>Should you wish to discuss any detail, please call our office and an advisor will arrange a time that suits you. We look forward to working together over the coming months.</p>
  </div>
  <div class="sign-block">47 Brookmere Loop West, Suite B318<br>Englewood, CO 80214<br>www.kt-assetpartners.com</div>
  <div class="artwork lower" role="img" aria-label="Blue block and silver arrow graphic"></div>
  <div class="footer-band"></div>
</section>

<section class="piece cd-folder" aria-label="CD folder">
  <svg width="290" height="290" viewBox="0 0 290 290" aria-hidden="true">
    <defs>
      <linearGradient id="folderFill" x1="0" y1="0" x2="1" y2="1">
        <stop offset="0" stop-color="#1f5fb8"/>
        <stop offset="1" stop-color="#071d4d"/>
      </linearGradient>
    </defs>
    <path d="M0 0H290V110A40 40 0 0 0 290 190V290H0Z" fill="url(#folderFill)"/>
  </svg>
  <div class="brand on-dark"><span class="brand-mark"></span>Harvest Ledger Group</div>
  <div class="artwork" role="img" aria-label="Blue blocks and silver arrow graphic" style="left:40px;top:80px;width:200px;height:190px;clip-path:polygon(10% 30%,100% 0,90% 100%,0 100%);opacity:.85"></div>
</section>

<section class="piece cd-disc" aria-label="CD disc">
  <div class="artwork" role="img" aria-label="Blue blocks and silver arrow graphic"></div>
  <div class="web">www.kt-assetpartners.com</div>
</section>

<section class="piece sleeve" aria-label="CD sleeve">
  <div class="flap"></div>
  <div class="brand on-dark"><span class="brand-mark"></span>Harvest Ledger Group</div>
  <div class="note-lines"></div>
  <div class="web">www.kt-assetpartners.com</div>
</section>

<section class="piece logo-lockup" aria-label="Logo">
  <div class="brand on-dark"><span class="brand-mark"></span>Harvest Ledger Group</div>
  <div class="tagline">Comprehensive financial and estate planning</div>
</section>

</body>
</html>
```